Fun, challenging, and inspirational guide for life change - written by a coach, therapist and founde

I need (1) cover design for a book titled:
"THE WANDERER'S TOOLKIT FOR MIND-SHIFTING IDEAS" - the surprisingly practical magic of believing and taking action

A 2ND COVER will be need for a companion ebook, titled:
"THE HEARTH LEDGER FOR PURPOSE AND CONTENTMENT - 3 steps to help unlock and unleash the unlimited you by loving your limitations

These books will be used to promote a larger suite of products and services devoted to empowering and inspiring a community of OVERCOMERS.

For reference check out www.brightquillpath.com

I've included some photos for visual reference points.

DESIGNS CONCEPTS:
CLEAN - A BLEND OF PAST AND PRESENT - MODERN AND THE SACRED) (...The Marlowe's Atlas meets

Target Market(s)

young and aspiring professionals and seasoned pros looking for life-changes due to feeling unfulfilled in their profession and relationships

Industry/Entity Type

Life Coaching

Font styles to use
Serif
Sans Serif

Requirements
Must have
• CREATIVITY - ORIGINALITY - WICKEDLY CLEAN DESIGN- AND IMPACTFUL TRANSLATION OF BRAND CONCEPT - COLOR AND PUNCH
Nice to have
• I included some photos as reference point - **PLEASE SEE THE PHOTOS FOR THE STAR-GAZERS DESIGNS** - I really like the feeling they provoke - I want to give the viewer a sense of the journey that can be taken when they dive into these books.
• Basically, riff off the design profiles and colors included in the STAR-GAZER covers.
• MUSTS INCLUDE -
• -ORIGINALITY
• - IMPACT
• - COLOR
• - ORIGINAL DESIGNS+
• +
Should not have
• STAY AWAY FROM...
• 1 OVERUSED AND TRENDY ICONS
• - ESOTERIC IMAGES
• - FLOWERY SCRIPTS
• - I AM REALLY LOOKING FOR A UPDATE OF THE TYPICAL SELF-HELP BOOK COVERS WHICH RELY TOO MUCH ON FLOWERY AND SACRED IMAGERY
• THANK YOU - feel free to unleash your creativity!

```html
<!DOCTYPE html>
<html lang="en">
<head>
<meta charset="utf-8">
<title>The Wanderer's Toolkit for Mind-Shifting Ideas</title>
<link rel="stylesheet" href="https://fonts.googleapis.com/css2?family=Comfortaa:wght@400&family=Lato:wght@400&display=swap">
<style>
  :root {
    --green-deep: #1f5e52;
    --green-mid: #2a7d68;
    --green-light: #37a082;
    --ink-light: #ffffff;
    --emblem-tint: rgba(255, 255, 255, 0.14);
  }
  html, body {
    margin: 0;
    padding: 0;
    overflow: hidden;
  }
  .book-cover {
    position: relative;
    width: 800px;
    height: 1200px;
    overflow: hidden;
    background: linear-gradient(to bottom, var(--green-deep) 0%, var(--green-mid) 50%, var(--green-light) 100%);
    color: var(--ink-light);
  }
  .cover-emblem {
    position: absolute;
    left: 230px;
    top: 338px;
    width: 340px;
    height: 192px;
  }
  .cover-title {
    position: absolute;
    top: 678px;
    left: 0;
    width: 100%;
    margin: 0;
    text-align: center;
    font-family: "Comfortaa", sans-serif;
    font-weight: 400;
    font-size: 42px;
    line-height: 68px;
    letter-spacing: 1px;
    text-transform: uppercase;
  }
  .cover-title span {
    display: block;
  }
  .cover-subtitle {
    position: absolute;
    top: 918px;
    left: 0;
    width: 100%;
    margin: 0;
    text-align: center;
    font-family: "Lato", sans-serif;
    font-size: 22px;
    line-height: 33px;
    letter-spacing: 0.3px;
  }
  .cover-subtitle span {
    display: block;
  }
</style>
</head>
<body>
  <main class="book-cover">
    <svg class="cover-emblem" viewBox="0 0 340 192" role="img" aria-label="Line-art emblem: a pair of spread wings beneath an interlocking circle motif">
      <rect x="0" y="0" width="340" height="192" rx="24" fill="var(--emblem-tint)"/>
    </svg>
    <h1 class="cover-title">
      <span>The Wanderer's Toolkit</span>
      <span>for</span>
      <span>Mind-Shifting Ideas</span>
    </h1>
    <p class="cover-subtitle">
      <span>11 beliefs to unlock and unleash your</span>
      <span>passion and purpose on the world</span>
    </p>
  </main>
</body>
</html>
```